Advert for e-news letter

I have a property valuation business and this is an advert for one specific service. The service is for Lot Entitlements and is directed at conveyancers. I have attached a company logo. The sizing of the advert (as noted in Media kit) – will be 158px x 170 px.
Advert to summarise the following;
Do you have developer clients? We can help with Lot Entitlements for Land Division. We believe that our prices are the best in the market, however should you provide a cheaper written quote we will beat it by 15%.
Pricing for RVB compliant Lot Entitlement Certificates.
• 1 Allotment into 2 Community Titled Lots: $220 Inc GST (2 day turnaround)
• 1 Allotment into 3 Community Titled Lots: $275 Inc GST (2 day turnaround)
• 1 Allotment into 4 or 5 Community Titled Lots: $330 Inc GST (2 day turnaround)
• 6 or more or Commercial: By Quote

```html
<!DOCTYPE html>
<html lang="en">
<head>
<meta charset="utf-8">
<title>Lot Entitlements Advert</title>
<link href="https://fonts.googleapis.com/css2?family=Arimo:wght@400;700&display=swap" rel="stylesheet">
<style>
  :root {
    --frame: #1aa9e6;
    --blue-top: #0875bd;
    --blue-bottom: #74b1c9;
    --red-deep: #c81a3a;
    --red-soft: #ef6d6f;
    --white: #ffffff;
    --navy: #0f2747;
    --ink: #2a2a2a;
    --teal: #23b3a5;
  }
  html, body {
    margin: 0;
    padding: 0;
    width: 1150px;
    height: 1200px;
    overflow: hidden;
    background: var(--white);
    font-family: "Arimo", Arial, sans-serif;
  }
  .canvas {
    position: relative;
    width: 1150px;
    height: 1200px;
  }
  .advert {
    position: absolute;
    left: 222px;
    top: 242px;
    width: 656px;
    height: 705px;
    border: 3px solid var(--frame);
    overflow: hidden;
  }
  .advert-bg {
    position: absolute;
    inset: 0;
  }
  .brand {
    position: absolute;
    left: 46px;
    top: 44px;
    display: flex;
    align-items: center;
    gap: 14px;
  }
  .brand-mark {
    width: 34px;
    height: 34px;
    background: var(--teal);
  }
  .brand-name {
    font-weight: 700;
    font-size: 44px;
    color: var(--ink);
    letter-spacing: 1px;
  }
  .headline {
    position: absolute;
    right: 45px;
    top: 26px;
    margin: 0;
    text-align: right;
    color: var(--white);
    font-weight: 700;
    font-size: 42px;
    line-height: 54px;
  }
  .pitch {
    position: absolute;
    left: 33px;
    top: 155px;
    margin: 0;
    color: var(--white);
    font-size: 31px;
    line-height: 46px;
  }
  .pitch strong {
    font-size: 48px;
    font-weight: 700;
  }
  .pricing {
    position: absolute;
    left: 37px;
    top: 459px;
    color: var(--navy);
    font-size: 19.5px;
    line-height: 25px;
  }
  .pricing-title {
    margin: 0 0 4px;
    font-weight: 700;
  }
  .price-list {
    list-style: none;
    margin: 0;
    padding: 0;
  }
  .price-list li {
    margin-bottom: 4px;
    padding-left: 13px;
    text-indent: -13px;
  }
  .price-list li::before {
    content: "•";
    display: inline-block;
    width: 13px;
    text-indent: 0;
  }
  .turnaround {
    display: block;
    padding-left: 12px;
    text-indent: 0;
  }
</style>
</head>
<body>
<div class="canvas">
  <div class="advert">
    <svg class="advert-bg" width="656" height="705" viewBox="0 0 656 705" aria-hidden="true">
      <defs>
        <linearGradient id="blueFade" x1="0" y1="0" x2="0" y2="1">
          <stop offset="0.18" stop-color="var(--blue-top)"/>
          <stop offset="0.75" stop-color="var(--blue-bottom)"/>
          <stop offset="1" stop-color="#6eacc6"/>
        </linearGradient>
        <linearGradient id="redFade" x1="0" y1="0" x2="1" y2="0">
          <stop offset="0.35" stop-color="var(--red-deep)"/>
          <stop offset="1" stop-color="var(--red-soft)"/>
        </linearGradient>
      </defs>
      <rect width="656" height="705" fill="url(#blueFade)"/>
      <rect width="480" height="139" fill="var(--white)"/>
      <circle cx="545" cy="5" r="229" fill="var(--white)"/>
      <circle cx="545" cy="5" r="220" fill="url(#redFade)"/>
    </svg>

    <div class="brand">
      <span class="brand-mark"></span>
      <span class="brand-name">NVQ</span>
    </div>

    <h1 class="headline">Do you have<br>developer<br>clients?</h1>

    <p class="pitch">We can help with Lot<br>Entitlements for Land<br>Division. We believe that our prices are<br>the best in the market, however should<br>you provide a cheaper written quote we<br>will beat it by <strong>15%.</strong></p>

    <div class="pricing">
      <p class="pricing-title">Pricing for RVB compliant Lot Entitlement Certificates.</p>
      <ul class="price-list">
        <li>1 Allotment into 2 Community Titled Lots: $220 Inc GST<span class="turnaround">(2 day turnaround)</span></li>
        <li>1 Allotment into 3 Community Titled Lots: $275 Inc GST<span class="turnaround">(2 day turnaround)</span></li>
        <li>1 Allotment into 4 or 5 Community Titled Lots: $330 Inc GST<span class="turnaround">(2 day turnaround)</span></li>
        <li>6 or more or Commercial: By Quote</li>
      </ul>
    </div>
  </div>
</div>
</body>
</html>
```